GILDED BRICKWORK: THE DEPENDABLE ROUTE WHEREBY MODEST HOUSING FLIPS YIELD HANDSOME RETURNS

I am looking for a book cover design for my new E-Book.

My idea for the design is a pin board with before and after photos of our properties pinned on it (example attached). I have also attached some photos to use.

PLEASE SUBMIT OTHER DESIGNS ALSO AS THIS WAS JUST AN IDEA BUT I AM OPEN TO OTHER IDEAS ALSO.

Page size is 5x7 inches

Font styles to use
Serif
Sans Serif

Colors
0255a3
3176b5
85acd3
85cae6
33a6d7
0392cd
9bcb3c
abd036
ec1f27

```html
<!DOCTYPE html>
<html lang="en">
<head>
<meta charset="utf-8">
<title>Gilded Brickwork – Book Cover</title>
<link href="https://fonts.googleapis.com/css2?family=Oswald:wght@300;400;500&display=swap" rel="stylesheet">
<style>
  :root {
    --sky-top: #46548a;
    --sky-mid: #6f86bd;
    --sky-low: #9ab0d8;
    --horizon: #d9a3a8;
    --house: #5a6478;
    --street: #2f3644;
    --title: #ffffff;
    --band: #f4eedb;
    --author: #1f2a3c;
  }
  html, body {
    margin: 0;
    padding: 0;
    width: 800px;
    height: 1200px;
    overflow: hidden;
    background: #ffffff;
  }
  .cover {
    position: relative;
    width: 800px;
    height: 1200px;
    overflow: hidden;
    font-family: "Oswald", sans-serif;
  }
  .cover-photo {
    position: absolute;
    inset: 0 0 72px 0;
    background:
      linear-gradient(180deg,
        var(--sky-top) 0%,
        var(--sky-mid) 35%,
        var(--sky-low) 52%,
        var(--horizon) 60%,
        var(--house) 66%,
        #4a5366 84%,
        var(--street) 100%);
  }
  .title {
    position: absolute;
    top: 40px;
    left: 0;
    right: 0;
    margin: 0;
    text-align: center;
    color: var(--title);
    font-weight: 400;
    font-size: 148px;
    line-height: 170px;
    letter-spacing: 10px;
    text-shadow: 0 3px 8px rgba(0, 0, 0, 0.25);
  }
  .title span { display: block; }
  .subtitle {
    position: absolute;
    top: 480px;
    left: 60px;
    right: 60px;
    margin: 0;
    text-align: center;
    color: var(--title);
    font-weight: 400;
    font-size: 20px;
    line-height: 34px;
    letter-spacing: 2px;
    text-shadow: 0 2px 4px rgba(0, 0, 0, 0.3);
  }
  .author-band {
    position: absolute;
    left: 0;
    right: 0;
    bottom: 0;
    height: 72px;
    background: var(--band);
    display: flex;
    align-items: center;
    justify-content: center;
  }
  .author {
    margin: 0;
    color: var(--author);
    font-weight: 500;
    font-size: 40px;
    letter-spacing: 9px;
  }
</style>
</head>
<body>
  <main class="cover">
    <div class="cover-photo" role="img" aria-label="Photograph of a renovated two-storey suburban house with lit windows and a double garage at dusk, under a blue and pink evening sky, wet street in front"></div>
    <h1 class="title"><span>GILDED</span><span>BRICKWORK</span></h1>
    <p class="subtitle">THE DEPENDABLE ROUTE WHEREBY MODEST<br>HOUSING FLIPS YIELD HANDSOME RETURNS</p>
    <footer class="author-band">
      <p class="author">MARTIN CALDWELL</p>
    </footer>
  </main>
</body>
</html>
```